Web design for a french company scanning and analyzing road infrastructures

Veltrane is a French company specializing in the digitization and advanced analysis of road infrastructures.

The current site consists of a single landing page.

We would now like to expand the site to detail the services we offer.

We would therefore like to have several pages created:
- redesign of the home page
- “traffic intersection” study page: Veltrane offers several studies, so we need to create a template for these studies, using the theme of traffic intersections as an example.
- “horizontal marking” service page: The studies are made up of services (simple post-processing). There will be multiple services. Here too, we need to create a template for these services, with the "horizontal marking " service as an example.

Elements to keep (all of them are available in the links below) :
- The Veltrane logo, which must be kept as is, including colors.
- Existing product and service illustrations and videos.
- Existing texts must be kept as they are, in terms of wording and hierarchy, to guarantee the accuracy of the information provided.
- Links to the current "home" (https://veltrane.example/), "traffic intersection" (https://veltrane.example/etudes/intersection/) and "horizontal marking" (https://veltrane.example/post-traitements/signalisation-horizontale-2-2/ ) pages.

Creative guidelines :
- Elegance: Design should communicate elegance while remaining accessible.
- Modernity and Innovation: Draw inspiration from the latest trends in web design to convey our commitment to innovation.
- Content enhancement: The layout should emphasize textual and visual content in a balanced and harmonious way.

To achieve this, you have the option of changing typography, colors (excluding logo), generic illustrations (i.e. not specific to our products and services), and integrating pictograms as required.

Delivery of files :
- Files must be created in Photoshop or Illustrator.
- They must include mock-ups for smartphone, tablet and PC screen resolutions of 1280px and higher.

```html
<!DOCTYPE html>
<html lang="fr">
<head>
<meta charset="utf-8">
<title>Veltrane — Numérisation et analyse des infrastructures routières</title>
<link rel="stylesheet" href="https://fonts.googleapis.com/css2?family=Michroma&family=Lexend+Exa:wght@400;500&family=Open+Sans:wght@400;600&display=swap">
<style>
:root{
  --canvas:#040d07;
  --page:#000000;
  --panel:#1d1d1f;
  --tab:#232325;
  --text:#ffffff;
  --muted:#cfcfd4;
  --blue:#3340ff;
  --violet:#6f5bff;
  --green:#1fe04a;
  --green-dark:#0d7a26;
  --line:#2e2e33;
}
*{margin:0;padding:0;box-sizing:border-box}
html,body{width:1200px;height:3677px;overflow:hidden}
body{
  background:radial-gradient(ellipse at 50% 100%,#0b2a12 0%,var(--canvas) 60%);
  font-family:"Open Sans",sans-serif;color:var(--text);position:relative;
}
.page{position:absolute;left:111px;top:1147px;width:978px;height:2530px;background:var(--page);overflow:hidden}
.abs{position:absolute}

/* nav */
.brand{left:86px;top:28px;display:flex;align-items:center;gap:10px;font-family:"Michroma",sans-serif;font-size:20px;letter-spacing:2px;color:var(--green)}
.brand-mark{width:18px;height:18px;background:var(--green)}
.nav-link{top:37px;font-family:"Lexend Exa",sans-serif;font-size:9px;font-weight:500;letter-spacing:.3px;color:var(--text)}
.btn{border:1.5px solid var(--green-dark);border-radius:16px;color:var(--green);font-family:"Lexend Exa",sans-serif;font-size:9px;display:flex;align-items:center;justify-content:center;background:#050505}

/* hero */
.hero{left:0;top:0;width:978px;height:559px}
.hero-visual{position:absolute;inset:0;background:
  linear-gradient(90deg,rgba(0,0,0,0) 0%,rgba(0,0,0,.2) 40%,#000 75%),
  linear-gradient(160deg,#3a1450 0%,#5a2a6a 18%,#b8391f 38%,#e08a22 52%,#c12a1a 62%,#2a0f3a 78%,#000 100%)}
.hero-line{left:0;width:978px;text-align:center;font-family:"Lexend Exa",sans-serif;font-size:29px;font-weight:500;letter-spacing:.5px}
.accent{background:linear-gradient(90deg,var(--blue),var(--violet));-webkit-background-clip:text;background-clip:text;color:transparent}
.ghost-clip{left:540px;top:190px;width:164px;height:190px;overflow:hidden}
.ghost{font-family:"Lexend Exa",sans-serif;font-size:31px;font-weight:500;color:#3a3a3e;white-space:nowrap;position:absolute;left:15px}

/* product */
.product-visual{left:53px;top:688px;width:499px;height:392px;background:
  radial-gradient(circle at 38% 48%,#f2f2f2 0%,#b8b8c8 30%,#3c46e0 48%,rgba(0,0,0,0) 62%),
  linear-gradient(180deg,#000 70%,#0a1e6a 90%,#000 100%)}
.section-title{font-family:"Michroma",sans-serif;font-size:28px;letter-spacing:1px}
.body-copy{font-size:10px;line-height:14px;color:var(--muted)}
.body-copy p+p{margin-top:14px}

.media{background:#222}
.video-bar{left:0;bottom:0;width:100%;height:22px;background:linear-gradient(0deg,rgba(0,0,0,.8),rgba(0,0,0,0));display:flex;align-items:center;padding:0 6px;gap:8px;font-size:7px}
.compare-handle{width:30px;height:30px;border-radius:50%;background:var(--green);display:flex;align-items:center;justify-content:center;font-size:10px;color:#000;font-weight:600}

.glow{left:880px;top:1420px;width:150px;height:150px;border-radius:50%;background:radial-gradient(circle,#2a35ff 0%,rgba(20,30,200,.5) 40%,rgba(0,0,0,0) 70%)}

/* tabs */
.panel{left:83px;top:1561px;width:806px;height:361px;background:var(--panel);border:1.5px solid var(--green-dark);border-radius:12px}
.tab{top:1537px;height:43px;border-radius:12px 12px 6px 6px;background:var(--tab);border:1px solid var(--line);font-family:"Lexend Exa",sans-serif;font-size:9.5px;display:flex;align-items:center;justify-content:center;color:var(--text)}
.tab.is-active{background:linear-gradient(90deg,var(--blue),var(--green));border:none}
.panel-visual{left:120px;top:1615px;width:351px;height:253px;border:1px solid var(--blue);background:linear-gradient(135deg,#3a3a3a 0%,#8a8a8a 35%,#2a8a3a 55%,#bdbdbd 75%,#222 100%)}
.panel-title{left:525px;top:1643px;font-family:"Lexend Exa",sans-serif;font-size:17px;font-weight:500}
.panel-copy{left:525px;width:300px}

/* clients */
.floor{left:0;top:2300px;width:978px;height:230px;background:linear-gradient(180deg,rgba(0,0,0,0) 0%,#06124a 55%,#0a2090 100%)}
.card{border:2px solid var(--green);overflow:hidden}
.card-photo{position:absolute;inset:0}
.card-shade{position:absolute;inset:0;background:linear-gradient(180deg,rgba(0,0,0,0) 35%,rgba(0,0,0,.85) 70%)}
.card-title{position:absolute;left:28px;top:188px;font-family:"Lexend Exa",sans-serif;font-size:18px;color:var(--green)}
.card-rule{position:absolute;left:28px;top:216px;width:50px;height:2px;background:var(--green)}
.card-copy{position:absolute;left:28px;top:230px;width:200px;font-size:10px;line-height:14px;color:#e6e6e6}
</style>
</head>
<body>
<main class="page">

  <section class="hero abs">
    <div class="hero-visual" role="img" aria-label="Nuage de points coloré d'une chaussée scannée"></div>
    <div class="brand abs"><span class="brand-mark"></span>VELTRANE</div>
    <a class="nav-link abs" style="left:395px">PRODUIT</a>
    <a class="nav-link abs" style="left:464px">NOS POST-TRAITEMENTS</a>
    <a class="nav-link abs" style="left:622px">NOS CLIENTS</a>
    <a class="nav-link abs" style="left:716px">NOTRE EQUIPE</a>
    <a class="btn abs" style="left:809px;top:26px;width:87px;height:30px">CONTACT</a>

    <div class="ghost-clip abs">
      <span class="ghost" style="top:10px">Technologie</span>
      <span class="ghost" style="top:140px">Analyse automatisée</span>
    </div>
    <h1 class="hero-line abs" style="top:208px">Technologie <span class="accent">unique</span></h1>
    <p class="hero-line abs" style="top:258px">Précision topo<span class="accent">graphique</span></p>
    <p class="hero-line abs" style="top:301px">Analyse auto<span class="accent">matisée</span></p>
    <a class="btn abs" style="left:445px;top:370px;width:86px;height:30px">CONTACT</a>
  </section>

  <div class="product-visual abs" role="img" aria-label="Boîtier de numérisation mobile Terrakit sur un sol quadrillé bleu"></div>
  <h2 class="section-title abs" style="left:549px;top:724px">VELT<span class="accent">RANE</span></h2>
  <div class="body-copy abs" style="left:551px;top:780px;width:300px">
    <p>Issu de plusieurs années de R&amp;D et de plus de 10 ans d'expertise dans le domaine de la fusion de données, le « Terrakit » combine système de positionnement breveté et automatisation des traitements par IA pour numériser l'environnement avec une précision absolue, de façon mobile.</p>
    <p>Notre Terrakit intègre les technologies avancées de numérisation 3D et un système de géopositionnement breveté.<br>Nos algorithmes de post traitement par IA permettent l'exploitation automatique des nuages de points.</p>
    <p>Cette technologie exclusive nous permet de réaliser des inventaires exhaustifs et des analyses de conformités de vos structures routières, à grand rendement et à coût maîtrisé.</p>
  </div>
  <a class="btn abs" style="left:551px;top:1043px;width:126px;height:29px;font-family:'Open Sans',sans-serif;font-size:10px">Notre technologie</a>

  <div class="media abs" style="left:83px;top:1180px;width:399px;height:217px">
    <div class="abs" style="inset:0;background:linear-gradient(180deg,#6f7f6a 0%,#9aa0a4 45%,#5a5d62 70%,#3b3d40 100%)" role="img" aria-label="Vidéo d'un véhicule équipé du scanner circulant en ville"></div>
    <div class="video-bar abs"><span>▶</span><span>0:00 / 0:40</span></div>
  </div>
  <div class="media abs" style="left:504px;top:1190px;width:388px;height:193px;overflow:hidden">
    <div class="abs" style="left:0;top:0;width:194px;height:193px;background:linear-gradient(180deg,#2e6a2a 0%,#2a2a2a 25%,#111 100%)" role="img" aria-label="Chaussée scannée en niveaux de gris"></div>
    <div class="abs" style="left:194px;top:0;width:194px;height:193px;background:linear-gradient(180deg,#2fbf3a 0%,#d80fd8 35%,#e020e0 100%)" role="img" aria-label="Chaussée classifiée par l'algorithme"></div>
    <div class="abs" style="left:193px;top:0;width:2px;height:193px;background:var(--green)"></div>
    <div class="compare-handle abs" style="left:179px;top:82px">‹›</div>
  </div>

  <div class="glow abs"></div>
  <h2 class="section-title abs" style="left:0;width:978px;text-align:center;top:1475px">POST-<span class="accent">TRAITEMENTS</span></h2>

  <div class="panel abs"></div>
  <a class="tab is-active abs" style="left:106px;width:181px">Signalisation horizontale</a>
  <a class="tab abs" style="left:295px;width:190px">Signalisation horizontale</a>
  <a class="tab abs" style="left:498px;width:181px">Dispositifs de retenue</a>
  <a class="tab abs" style="left:688px;width:182px">Etat de la chaussée</a>

  <div class="panel-visual abs" role="img" aria-label="Vue aérienne d'un carrefour avec marquages détectés et loupe sur un passage piéton"></div>
  <h3 class="panel-title abs">Etat de la chaussée</h3>
  <p class="panel-copy body-copy abs" style="top:1693px">Grâce au jumeau numérique créé par notre Terrakit, nos algorithmes d'intelligence artificielle sont capables de détecter et d'évaluer l'état de tous les éléments de signalisation horizontale présents sur les voies scannées.</p>
  <p class="panel-copy body-copy abs" style="top:1765px">Grâce au jumeau numérique créé par notre Terrakit, nos algorithmes d'intelligence artificielle sont capables de détecter et d'évaluer l'état de tous les éléments de signalisation horizontale présents sur les voies scannées.</p>

  <div class="floor abs" role="img" aria-label="Sol quadrillé bleu en perspective"></div>
  <h2 class="section-title abs" style="left:0;width:978px;text-align:center;top:2005px">NOS <span class="accent">CLIENTS</span></h2>

  <article class="card abs" style="left:81px;top:2093px;width:259px;height:357px">
    <div class="card-photo" style="background:linear-gradient(180deg,#4d7fc4 0%,#9ab4d8 35%,#6b6258 60%,#2a2622 100%)" role="img" aria-label="Façade d'une mairie"></div>
    <div class="card-shade"></div>
    <h3 class="card-title">Collectivités</h3><span class="card-rule"></span>
    <p class="card-copy">Grâce au jumeau numérique créé par notre Terrakit, nos algorithmes d'intelligence artificielle sont capables de détecter et d'évaluer l'état de tous les éléments de signalisation horizontale présents sur les voies scannées.</p>
  </article>
  <article class="card abs" style="left:351px;top:2085px;width:273px;height:372px">
    <div class="card-photo" style="background:linear-gradient(180deg,#8aa0b8 0%,#c5cdd6 30%,#5b5f55 55%,#3a3a3a 100%)" role="img" aria-label="Géomètre avec son instrument au bord d'une route"></div>
    <div class="card-shade"></div>
    <h3 class="card-title" style="top:192px">Géomètres</h3><span class="card-rule" style="top:220px"></span>
    <p class="card-copy" style="top:234px;width:215px">Nous proposons aux géomètres une solution alternative, efficiente et économique aux moyens de numérisation classiques.</p>
  </article>
  <article class="card abs" style="left:634px;top:2093px;width:259px;height:357px">
    <div class="card-photo" style="background:linear-gradient(180deg,#8a8a8a 0%,#6a6a6a 40%,#9a8a40 60%,#2a2a2a 100%)" role="img" aria-label="Ingénieurs consultant un plan routier"></div>
    <div class="card-shade"></div>
    <h3 class="card-title">Bureaux d'étude</h3><span class="card-rule"></span>
    <p class="card-copy">Grâce au jumeau numérique créé par notre Terrakit, nos algorithmes d'intelligence artificielle sont capables de détecter et d'évaluer l'état de tous les éléments de signalisation horizontale présents sur les voies scannées.</p>
  </article>

</main>
</body>
</html>
```